【依頼の目的/概要】
電子書籍(vellis)の表紙デザインをお願いします。

【画像サイズ】 ※VSRより抜粋
表紙ファイルの理想的な寸法 2,560×1,600ピクセルです。
注:画像の寸法は 1,000×625ピクセル以上であることが必要です。
画像の最大の寸法は 10,000×10,000ピクセルです。

【タイトル】

港町の料理人へ贈る
季節ごとに変わる庭の手入れがわかる
「月灯り菜園ノート」

【著者】

MIRO

【本の内容】

5つの窓辺・ロカルナ年代記などの人間心理・成功本から
パートナーに関する知識をまとめて解説した本です。

※本文を参考資料として添付します。

【デザイン要望】

特にイメージにこだわりはありませんので、
自由な発送でのデザインご応募を楽しみにしています。

※次点、次々点の方への参加報酬を設定致しました。

※その他 必要な情報がありましたら、お問い合わせください。

ターゲット層がリアル風が好きだと思ったので、選びました

今回も多数応募頂きまして、誠にありがとうございました。

```html
<!DOCTYPE html>
<html lang="ja">
<head>
<meta charset="utf-8">
<title>月灯り菜園ノート — 表紙</title>
<link href="https://fonts.googleapis.com/css2?family=Noto+Sans+JP:wght@500;700;900&family=Cutive+Mono&display=swap" rel="stylesheet">
<style>
  :root {
    --ink: #ffffff;
    --shadow: #000000;
    --photo-highlight: #d9d9d9;
    --photo-light: #a8a8a8;
    --photo-mid: #6a6a6a;
    --photo-deep: #2a2a2a;
    --photo-dark: #050505;
  }
  html, body {
    margin: 0;
    padding: 0;
    width: 750px;
    height: 1200px;
    overflow: hidden;
    background: var(--photo-dark);
  }
  .cover {
    position: relative;
    width: 750px;
    height: 1200px;
    overflow: hidden;
    font-family: "Noto Sans JP", sans-serif;
    color: var(--ink);
  }
  .cover-photo {
    position: absolute;
    inset: 0;
    background:
      radial-gradient(ellipse 22% 40% at 30% 78%, var(--photo-dark) 0%, var(--photo-dark) 55%, transparent 100%),
      radial-gradient(ellipse 30% 48% at 80% 72%, var(--photo-dark) 0%, var(--photo-dark) 60%, transparent 100%),
      radial-gradient(ellipse 16% 14% at 51% 38%, var(--photo-light) 0%, transparent 100%),
      radial-gradient(ellipse 38% 16% at 60% 16%, var(--photo-highlight) 0%, transparent 100%),
      radial-gradient(ellipse 30% 22% at 12% 22%, var(--photo-deep) 0%, transparent 100%),
      linear-gradient(180deg, var(--photo-mid) 0%, #8a8a8a 22%, var(--photo-mid) 40%, #3a3a3a 47%, var(--photo-deep) 50%, #121212 72%, var(--photo-dark) 100%);
  }
  .title-main {
    position: absolute;
    margin: 0;
    font-weight: 900;
    line-height: 1;
    text-shadow: 0 0 6px var(--shadow), 3px 3px 0 var(--shadow);
  }
  .title-line-1 { left: 24px; top: 16px; font-size: 92px; }
  .title-line-2 { left: 24px; top: 140px; font-size: 92px; }
  .title-tail { left: 462px; top: 292px; font-size: 54px; font-weight: 700; }
  .subtitle {
    position: absolute;
    left: 214px;
    top: 380px;
    margin: 0;
    writing-mode: vertical-rl;
    font-size: 35px;
    font-weight: 700;
    line-height: 1;
    text-shadow: 0 0 5px var(--shadow);
  }
  .series-title {
    position: absolute;
    left: 276px;
    top: 262px;
    margin: 0;
    writing-mode: vertical-rl;
    font-size: 72px;
    font-weight: 700;
    line-height: 1;
    text-shadow: 0 0 6px var(--shadow), 2px 2px 0 var(--shadow);
  }
  .author {
    position: absolute;
    left: 487px;
    top: 1008px;
    width: 226px;
    margin: 0;
    font-family: "Cutive Mono", monospace;
    font-size: 54px;
    line-height: 1.45;
    text-align: center;
    letter-spacing: 2px;
    text-shadow: 0 0 6px var(--shadow);
  }
  .author span { display: block; }
</style>
</head>
<body>
  <main class="cover">
    <div class="cover-photo" role="img" aria-label="モノクロ写真:上部に重ねた手のクローズアップ、下部に明るい背景の前で向かい合う二人のシルエット"></div>

    <h1 class="title-main title-line-1">港町の</h1>
    <p class="title-main title-line-2">料理人</p>
    <p class="title-main title-tail">へ贈る</p>

    <p class="subtitle">季節ごとに変わる庭の手入れがわかる</p>
    <p class="series-title">「月灯り菜園ノート」</p>

    <p class="author"><span>Author</span><span>MIRO</span></p>
  </main>
</body>
</html>
```